Kelvo App - Live Events Stream

Need mobile first appliation designs for a new location based events and offers application <br/><br/>Will require at least 5 screens creating, namely:<br/><br/>- Landing screen<br/>- Event/Offer listings screen<br/>- Overview of Event/Offer screen<br/>- Chat/Stream for Event/Offer<br/>- Directions for Event/Offer<br/>- Create Event/Offer screen(s)<br/><br/>Will require the design to have a vantor material feel. <br/><br/>See Attached files for further details

Requirements
Must have
• See Doc
Nice to have
• See Doc
Should not have
• See Doc

```html
<!DOCTYPE html>
<html lang="en">
<head>
<meta charset="utf-8">
<title>Kelvo – Create your event</title>
<link rel="stylesheet" href="https://fonts.googleapis.com/css2?family=Source+Sans+3:wght@600;700;800&display=swap">
<style>
  :root {
    --blue: #0088dd;
    --violet: #4f43a6;
    --magenta: #900070;
    --mint: #1ef5c8;
    --lime: #d2ff66;
    --panel: #d6d6fe;
    --field: #d2fefd;
    --ink: #0a0a14;
    --icon: #b984f8;
    --white: #ffffff;
  }
  * { box-sizing: border-box; margin: 0; padding: 0; }
  html, body { width: 1200px; height: 2458px; overflow: hidden; }
  body {
    position: relative;
    background: linear-gradient(90deg, var(--blue), var(--violet) 45%, var(--magenta));
    font-family: "Source Sans 3", "Myriad Pro", sans-serif;
    color: var(--ink);
  }
  .panel-shape { position: absolute; left: 0; top: 0; width: 1200px; height: 2458px; }
  .back { position: absolute; left: 70px; top: 56px; width: 60px; height: 80px; }
  .screen-title {
    position: absolute; left: 221px; top: 52px;
    font-size: 58px; font-weight: 700; letter-spacing: 10px; line-height: 1;
    background: linear-gradient(90deg, var(--mint), var(--lime));
    -webkit-background-clip: text; background-clip: text; color: transparent;
  }
  .tabs { position: absolute; top: 352px; left: 0; width: 1200px; height: 40px; }
  .tab {
    position: absolute; top: 0; transform: translateX(-50%);
    font-size: 34px; font-weight: 700; letter-spacing: 6px; line-height: 40px; color: var(--ink);
  }
  .tab-events { left: 270px; }
  .tab-streaming { left: 618px; }
  .tab-other { left: 952px; }
  .field-label {
    position: absolute; left: 62px;
    font-size: 35px; font-weight: 700; letter-spacing: 6px; line-height: 40px;
  }
  .field {
    position: absolute; left: 52px; width: 1096px;
    padding: 19px;
    background: linear-gradient(90deg, var(--blue), var(--violet) 45%, var(--magenta));
  }
  .field-inner { width: 100%; height: 100%; background: var(--field); }
  .field-name { top: 599px; height: 207px; border-radius: 68px; }
  .field-name .field-inner { border-radius: 50px; }
  .field-desc { top: 935px; height: 472px; border-radius: 100px; }
  .field-desc .field-inner { border-radius: 82px; }
  .field-tagline { top: 1547px; height: 399px; border-radius: 92px; }
  .field-tagline .field-inner { border-radius: 74px; }
  .field-location { top: 2056px; height: 420px; border-radius: 92px; }
  .field-location .field-inner { border-radius: 74px; }
  .nav-bar {
    position: absolute; left: 76px; top: 2240px; width: 1048px; height: 178px;
    background: var(--white); border-radius: 89px;
  }
  .nav-icon { position: absolute; top: 25px; width: 128px; height: 128px; }
  .nav-list { left: 41px; }
  .nav-mail { left: 251px; }
  .nav-mascot { left: 447px; width: 160px; top: 30px; height: 120px; }
  .nav-target { left: 669px; }
  .nav-compass { left: 879px; }
  .mascot-fill { width: 100%; height: 100%; border-radius: 50% 50% 40% 40%; background: #e6d6fd; }
</style>
</head>
<body>
  <svg class="panel-shape" viewBox="0 0 1200 2458" aria-hidden="true">
    <path fill="#d6d6fe" d="M0,2458 L0,530 C0,465 50,412 115,403 C124,401 130,394 130,385 L130,382 C130,354 152,332 180,332 L353,332 C381,332 403,354 403,382 C403,394 410,402 421,402 L1070,402 C1142,402 1200,460 1200,530 L1200,2458 Z"/>
  </svg>

  <svg class="back" viewBox="0 0 60 80" aria-label="Back">
    <defs>
      <linearGradient id="backGrad" x1="0" y1="0" x2="1" y2="1">
        <stop offset="0" stop-color="#1ef5c8"/><stop offset="1" stop-color="#d2ff66"/>
      </linearGradient>
    </defs>
    <polyline points="44,10 12,40 44,70" fill="none" stroke="url(#backGrad)" stroke-width="11" stroke-linecap="round" stroke-linejoin="round"/>
  </svg>
  <h1 class="screen-title">create your event</h1>

  <nav class="tabs">
    <span class="tab tab-events">Events</span>
    <span class="tab tab-streaming">Streaming</span>
    <span class="tab tab-other">Other</span>
  </nav>

  <label class="field-label" style="top:533px">choose yoru event name</label>
  <div class="field field-name"><div class="field-inner"></div></div>

  <label class="field-label" style="top:872px">Describe your event</label>
  <div class="field field-desc"><div class="field-inner"></div></div>

  <label class="field-label" style="top:1483px">Select your tagline</label>
  <div class="field field-tagline"><div class="field-inner"></div></div>

  <label class="field-label" style="top:1995px">Select your location</label>
  <div class="field field-location"><div class="field-inner"></div></div>

  <div class="nav-bar">
    <svg class="nav-icon nav-list" viewBox="0 0 128 128" aria-label="Listings" fill="none" stroke="#b984f8" stroke-width="4">
      <path d="M112,30 A60,60 0 1 0 112,98"/>
      <path d="M120,44 A60,60 0 0 1 120,84"/>
      <line x1="30" y1="34" x2="36" y2="34"/><line x1="44" y1="34" x2="116" y2="34"/>
      <line x1="30" y1="64" x2="36" y2="64"/><line x1="44" y1="64" x2="124" y2="64"/>
      <line x1="30" y1="94" x2="36" y2="94"/><line x1="44" y1="94" x2="116" y2="94"/>
    </svg>
    <svg class="nav-icon nav-mail" viewBox="0 0 128 128" aria-label="Messages" fill="none" stroke="#b984f8" stroke-width="4">
      <path d="M30,14 A60,60 0 0 1 98,14"/>
      <path d="M112,28 A60,60 0 0 1 118,92"/>
      <path d="M104,108 A60,60 0 0 1 24,108"/>
      <path d="M10,92 A60,60 0 0 1 16,28"/>
      <polyline points="18,20 64,64 110,20"/>
      <line x1="18" y1="98" x2="46" y2="70"/><line x1="110" y1="98" x2="82" y2="70"/>
    </svg>
    <div class="nav-icon nav-mascot" role="img" aria-label="App mascot emblem"><div class="mascot-fill"></div></div>
    <svg class="nav-icon nav-target" viewBox="0 0 128 128" aria-label="Location" fill="none" stroke-width="4">
      <defs>
        <linearGradient id="targetGrad" x1="0" y1="0" x2="1" y2="0">
          <stop offset="0" stop-color="#1ef5c8"/><stop offset="1" stop-color="#d2ff66"/>
        </linearGradient>
      </defs>
      <g stroke="url(#targetGrad)">
        <path d="M58,4 A60,60 0 0 0 4,58"/><path d="M70,4 A60,60 0 0 1 124,58"/>
        <path d="M4,70 A60,60 0 0 0 58,124"/><path d="M124,70 A60,60 0 0 1 70,124"/>
        <line x1="64" y1="0" x2="64" y2="128"/><line x1="0" y1="64" x2="128" y2="64"/>
      </g>
    </svg>
    <svg class="nav-icon nav-compass" viewBox="0 0 128 128" aria-label="Directions" fill="none" stroke="#b984f8" stroke-width="4">
      <path d="M104,18 A60,60 0 0 0 10,104"/>
      <path d="M118,36 A60,60 0 0 1 24,110"/>
      <polygon points="18,110 52,58 112,18 74,76"/>
      <line x1="52" y1="58" x2="74" y2="76"/>
    </svg>
  </div>
</body>
</html>
```